Wealth management firm needs a business card design

Using my logo, create a business card that covers all of the regulatory wordings that I need. It must have - Registered Office 5-7 Pellinore Court, Edinburgh, EH9 2QW. Registered in Scotland under number SC738204. Corvell Wealth Management Ltd is an appointed representative of Quintor wealth management Ltd, which is authorised and regulated by the Monetary Standards Council.

Target Market(s)

professional clients

Industry/Entity Type

finance

Contact Information for Business Card

Corvell Wealth Management, Rupert Ashdown-Kerr, Director, 9 Tanner Row, Edinburgh, EH2 4NP. 07812 455 193, rupert.ashdown-kerr@corvellwealth.example , www.corvellwealth.example

Font styles to use
Serif

Colors
0054AA
0677BA
7BADD7
CADEEF
E8F1F8

Requirements
Must have
• regulatory wording in small text at bottom

```html
<!DOCTYPE html>
<html lang="en">
<head>
<meta charset="utf-8">
<title>Corvell Wealth Management – Business Card</title>
<link rel="stylesheet" href="https://fonts.googleapis.com/css2?family=Archivo:wght@400;700&family=Source+Serif+4:wght@600;700&display=swap">
<style>
  :root {
    --bg: #e4e5e9;
    --card: #fbfbfb;
    --brand-blue: #1a80ee;
    --ink: #17171c;
    --muted: #9a9a9e;
    --rule: #a8a8ac;
  }
  * { box-sizing: border-box; margin: 0; padding: 0; }
  html, body { width: 1200px; height: 800px; overflow: hidden; }
  body {
    background: var(--bg);
    display: flex;
    align-items: center;
    justify-content: center;
    gap: 40px;
  }
  .card {
    position: relative;
    width: 540px;
    height: 340px;
    background: var(--card);
    border-radius: 38px;
    box-shadow: 0 2px 6px rgba(0,0,0,.12);
  }

  /* Company side */
  .company-side .company-name {
    position: absolute;
    left: 0; right: 0; top: 96px;
    text-align: center;
    font-family: "Source Serif 4", Georgia, serif;
    font-weight: 600;
    font-size: 30px;
    color: var(--ink);
    display: flex;
    align-items: center;
    justify-content: center;
    gap: 12px;
  }
  .company-side .mark-dot {
    width: 22px; height: 22px;
    border-radius: 50%;
    background: var(--brand-blue);
  }
  .company-side .tagline {
    position: absolute;
    left: 0; right: 0; top: 146px;
    text-align: center;
    font-family: "Source Serif 4", Georgia, serif;
    font-weight: 700;
    font-size: 11px;
    letter-spacing: .2px;
    color: var(--ink);
  }
  .company-side .rule {
    position: absolute;
    left: 50px; right: 50px; top: 186px;
    border-top: 1px solid var(--rule);
  }
  .company-side .regulatory {
    position: absolute;
    left: 50px; right: 50px; top: 200px;
    text-align: center;
    font-family: "Archivo", Arial, sans-serif;
    font-size: 11.5px;
    line-height: 1.45;
    color: var(--muted);
  }

  /* Contact side */
  .contact-side .person {
    position: absolute;
    left: 44px; top: 42px;
    font-family: "Archivo", Arial, sans-serif;
  }
  .contact-side .person-name {
    font-weight: 700;
    font-size: 20px;
    line-height: 1.05;
    color: var(--brand-blue);
    text-transform: uppercase;
  }
  .contact-side .person-role {
    font-size: 14px;
    color: var(--ink);
    margin-top: 2px;
  }
  .contact-side .details {
    position: absolute;
    left: 44px; top: 168px;
    font-family: "Archivo", Arial, sans-serif;
    font-size: 14.5px;
    line-height: 1.35;
    color: var(--ink);
  }
  .contact-side .address { margin-bottom: 10px; }
  .contact-side .line {
    display: flex;
    align-items: center;
    gap: 8px;
  }
  .contact-side .line svg { width: 13px; height: 13px; flex: none; }
</style>
</head>
<body>

  <section class="card company-side" aria-label="Company side">
    <h1 class="company-name"><span class="mark-dot"></span>Corvell Wealth Management Ltd</h1>
    <p class="tagline">Personal Financial Advice</p>
    <div class="rule"></div>
    <p class="regulatory">
      Registered Office: 5-7 Pellinore Court, Edinburgh, EH9 2QW.
      Registered in Scotland under number SC738204. Corvell Wealth Management
      Ltd is an appointed representative of Quintor wealth management Ltd, which is
      authorised and regulated by the Monetary Standards Council.
    </p>
  </section>

  <section class="card contact-side" aria-label="Contact side">
    <div class="person">
      <h2 class="person-name">Rupert<br>Ashdown-Kerr</h2>
      <p class="person-role">Director</p>
    </div>
    <div class="details">
      <p class="address">9 Tanner Row<br>Edinburgh, EH2 4NP</p>
      <p class="line">
        <svg viewBox="0 0 14 14" aria-hidden="true"><rect x="3" y="1" width="8" height="12" rx="1.5" fill="none" stroke="#1a80ee" stroke-width="1.6"/><rect x="4.5" y="3" width="5" height="7" fill="#1a80ee"/></svg>
        07812 455 193
      </p>
      <p class="line">
        <svg viewBox="0 0 14 14" aria-hidden="true"><rect x="1" y="3" width="12" height="8.5" fill="#1a80ee"/><path d="M1 3 L7 8 L13 3" fill="none" stroke="#fff" stroke-width="1.2"/></svg>
        rupert.ashdown-kerr@corvellwealth.example
      </p>
      <p class="line">
        <svg viewBox="0 0 14 14" aria-hidden="true"><g fill="none" stroke="#1a80ee" stroke-width="1.2"><circle cx="7" cy="7" r="5.8"/><ellipse cx="7" cy="7" rx="2.6" ry="5.8"/><path d="M1.2 7h11.6M2.2 4h9.6M2.2 10h9.6"/></g></svg>
        www.corvellwealth.example
      </p>
    </div>
  </section>

</body>
</html>
```